Boutique Barre Studio in Geneva

Business card for pilates and dance studio. We are a brand new studio and love our fresh image with our yellow color. This business card is meant for our founder.

```html
<!DOCTYPE html>
<html lang="en">
<head>
<meta charset="utf-8">
<title>Barrelle Studio – Business Card</title>
<link rel="stylesheet" href="https://fonts.googleapis.com/css2?family=Nunito:wght@400;600;800&display=swap">
<style>
  :root {
    --page-bg: #cbcbcb;
    --card-yellow: #ecf866;
    --ink: #111111;
    --photo-light: #cfe6ec;
    --photo-mid: #b7d8e1;
    --photo-floor: #dfe6e6;
    --photo-figure: #3d6a73;
  }
  * { margin: 0; padding: 0; box-sizing: border-box; }
  html, body {
    width: 1200px; height: 846px; overflow: hidden;
    background: var(--page-bg);
    font-family: "Nunito", sans-serif;
    color: var(--ink);
  }
  .card {
    position: absolute;
    left: 346px;
    width: 508px; height: 290px;
    border-radius: 26px;
    overflow: hidden;
  }
  .card--front { top: 113px; background: var(--card-yellow); }
  .card--back { top: 441px; }

  .brand {
    position: absolute;
    font-weight: 600;
    color: var(--ink);
    line-height: 1;
    text-align: center;
  }
  .brand__name { display: block; font-size: 54px; letter-spacing: -1px; }
  .brand__sub { display: block; font-size: 19px; letter-spacing: 2px; margin-top: 2px; }
  .card--front .brand { left: 0; right: 0; top: 44px; }
  .card--back .brand { left: 42px; top: 32px; }

  .person { position: absolute; left: 56px; top: 168px; }
  .person__name { font-weight: 800; font-size: 16px; line-height: 24px; }
  .person__role { font-weight: 400; font-size: 15.5px; line-height: 24px; }

  .contact { position: absolute; left: 234px; top: 168px; list-style: none; }
  .contact__item {
    display: flex; align-items: center; gap: 8px;
    font-size: 15.5px; line-height: 24px;
  }
  .contact__icon { width: 20px; height: 20px; flex: none; }

  .divider {
    position: absolute; left: 57px; width: 394px; top: 227px;
    height: 1px; background: var(--ink);
  }
  .address {
    position: absolute; left: 0; right: 0; top: 235px;
    text-align: center; font-size: 15.5px;
  }

  .photo {
    position: absolute; inset: 0;
    background:
      radial-gradient(ellipse 60% 22% at 58% 60%, var(--photo-figure) 0%, rgba(61,106,115,0.55) 45%, rgba(61,106,115,0) 100%),
      linear-gradient(180deg, var(--photo-light) 0%, var(--photo-mid) 78%, var(--photo-floor) 84%, #e8ecea 100%);
  }
  .website {
    position: absolute; left: 0; right: 0; top: 252px;
    text-align: center; font-weight: 600; font-size: 15px; letter-spacing: 1px;
  }
</style>
</head>
<body>

<section class="card card--front">
  <div class="brand">
    <span class="brand__name">barrelle</span>
    <span class="brand__sub">STUDIO</span>
  </div>

  <div class="person">
    <p class="person__name">Mira Lindqvist</p>
    <p class="person__role">Founder</p>
  </div>

  <ul class="contact">
    <li class="contact__item">
      <svg class="contact__icon" viewBox="0 0 24 24" fill="none" stroke="#111" stroke-width="2" stroke-linejoin="round" aria-hidden="true">
        <path d="M6.5 3h3l1.5 4.5-2 1.5a11 11 0 0 0 6 6l1.5-2 4.5 1.5v3a2 2 0 0 1-2 2A17 17 0 0 1 4.5 5a2 2 0 0 1 2-2z"/>
      </svg>
      <span>+33 712 408 355</span>
    </li>
    <li class="contact__item">
      <svg class="contact__icon" viewBox="0 0 24 24" fill="none" stroke="#111" stroke-width="2" stroke-linejoin="round" aria-hidden="true">
        <rect x="2.5" y="5" width="19" height="14" rx="2.5"/>
        <path d="M3.5 6.5l8.5 6.5 8.5-6.5"/>
      </svg>
      <span>hello@barrelle-studio.com</span>
    </li>
  </ul>

  <div class="divider"></div>
  <p class="address">Rue des Tilleuls 12 / 1205 Geneva / Switzerland</p>
</section>

<section class="card card--back">
  <div class="photo" role="img" aria-label="Photo of a woman in teal activewear doing a glute bridge on a mat in a bright studio"></div>
  <div class="brand">
    <span class="brand__name">barrelle</span>
    <span class="brand__sub">STUDIO</span>
  </div>
  <p class="website">WWW.BARRELLE-STUDIO.COM</p>
</section>

</body>
</html>
```